Poster announcing University Web Analytics talk

We need a poster to announce an upcoming talk on Web Analytics at the local University. The event is addressed to final year students (mostly in Informatic Engineering, although other majors are wellcomed as well) who may be interested in specializing in this rising field.

The poster should present a brief list of the points we'll be addressing, as well as the place and time of the meeting. Also, it must feature our company logo (check the uploads section to find it) and our website url: http://www.brasslanternworks.net.

Texts for the poster:

Headline: "Get specialized in Web & Mobile Analytics"

Topics that will be covered:
- Introduction to Analytics, market, work opportunities
- Know the basics of an Analytics project: planning, phases, implementation
- Job bank: bring your CV!

Event information: "Thursday 20th June at the Escuela de Sistemas, Instituto Pelayo Norte". [A space to fill with the time must be provided here]

However, we'll be translating all the text to Spanish later, so we'll need a file where we can modify the text layers.
Updates

Thanks to all of you, we're receiving so many excellent works!

We had missed to include some important information on the brief - we didn't say anything about the colors, and we have been getting some designs based in dark colors. Now, it doesn't matter what colors you use, but we'd like better a brighter design (no matter if the color combination is more playful or either rather serious). This is going to be a free talk addressed to last year students, so we want to transmit a feeling of an interesting, easy and entertaining afternoon.

I hope these comments are helpful, please reach me with any question or comment. 

Thanks a lot again!
Nuria 
BL team

Target Market(s)

Final year students and graduates.

Industry/Entity Type

Bank

Requirements
Must have
• Design must be submitted in vector format, preferably .psd. We must be able to modify the text layers. Our logo (check the files section) and website url (http://www.brasslanternworks.net) must be included
Nice to have
• Illustrations making reference to Analytics (charts, statistics, code) and/or the internet will be a plus!

```html
<!DOCTYPE html>
<html lang="en">
<head>
<meta charset="utf-8">
<title>Get specialized in Web &amp; Mobile Analytics</title>
<link rel="stylesheet" href="https://fonts.googleapis.com/css2?family=Questrial&display=swap">
<style>
  :root {
    --paper: #ffffff;
    --leaf: #76b83f;
    --ocean: #1d6690;
    --signal: #e3231b;
    --device-light: #e9e7e2;
    --device-mid: #c9c6bf;
    --ink-white: #ffffff;
  }
  html, body {
    margin: 0;
    padding: 0;
    overflow: hidden;
    background: var(--paper);
  }
  .poster {
    position: relative;
    width: 828px;
    height: 1200px;
    overflow: hidden;
    background: var(--paper);
    font-family: "Questrial", "Century Gothic", sans-serif;
  }
  .backdrop {
    position: absolute;
    inset: 0;
  }
  .brand {
    position: absolute;
    top: 80px;
    right: 58px;
    display: flex;
    align-items: center;
    gap: 10px;
    color: var(--ocean);
    font-size: 24px;
    line-height: 1.05;
  }
  .brand-mark {
    width: 40px;
    height: 40px;
    background: var(--ocean);
  }
  .website {
    position: absolute;
    top: 134px;
    right: 58px;
    margin: 0;
    color: var(--ocean);
    font-size: 14px;
    line-height: 18px;
  }
  .hero-visual {
    position: absolute;
    left: 170px;
    top: 162px;
    width: 440px;
    height: 421px;
    border-radius: 6px;
    background: linear-gradient(160deg, var(--device-light) 0%, var(--device-mid) 100%);
  }
  .trend-line {
    position: absolute;
    inset: 0;
    pointer-events: none;
  }
  .content {
    position: absolute;
    left: 53px;
    right: 40px;
    top: 735px;
    color: var(--ink-white);
  }
  .headline {
    margin: 0 0 34px;
    font-weight: 400;
    font-size: 57px;
    line-height: 1.2;
    letter-spacing: 0.2px;
  }
  .topics {
    list-style: none;
    margin: 0;
    padding: 0;
    font-size: 20px;
    line-height: 1.35;
  }
  .topics li {
    position: relative;
    padding-left: 20px;
    margin-bottom: 16px;
  }
  .topics li::before {
    content: "";
    position: absolute;
    left: 0;
    top: 9px;
    width: 7px;
    height: 7px;
    border-radius: 50%;
    background: var(--ink-white);
  }
  .topics .topic-highlight {
    font-size: 25px;
  }
  .topics .topic-highlight::before {
    top: 12px;
  }
  .event-info {
    position: absolute;
    left: 50px;
    top: 1124px;
    width: 742px;
    height: 32px;
    margin: 0;
    box-sizing: border-box;
    border: 2px solid var(--ink-white);
    border-radius: 16px;
    color: var(--ink-white);
    font-size: 16.5px;
    line-height: 28px;
    padding-left: 16px;
    white-space: nowrap;
    overflow: hidden;
  }
</style>
</head>
<body>
<main class="poster">
  <svg class="backdrop" width="828" height="1200" viewBox="0 0 828 1200" aria-hidden="true">
    <path fill="var(--leaf)" d="M0,330 C80,480 160,590 240,650 C320,710 400,700 470,696 C620,688 740,655 828,622 L828,1200 L0,1200 Z"/>
    <path fill="none" stroke="var(--ocean)" stroke-width="13" d="M240,650 C320,710 400,700 470,696 C620,688 740,655 828,622"/>
  </svg>

  <div class="brand">
    <span class="brand-mark"></span>
    <span class="brand-name">Brass Lantern<br>Works</span>
  </div>
  <p class="website">http://www.brasslanternworks.net</p>

  <div class="hero-visual" role="img" aria-label="Open silver laptop seen from the side with a mobile phone standing on its keyboard"></div>

  <svg class="trend-line" width="828" height="1200" viewBox="0 0 828 1200" aria-hidden="true">
    <polyline points="237,492 355,380 445,410 640,238" fill="none" stroke="var(--signal)" stroke-width="8" stroke-linejoin="round"/>
    <polygon points="672,210 628,222 652,250" fill="var(--signal)"/>
  </svg>

  <section class="content">
    <h1 class="headline">Get specialized in<br>Web &amp; Mobile Analytics</h1>
    <ul class="topics">
      <li>Introduction to Analytics, market, work opportunities</li>
      <li>Know the basics of an Analytics project: planning,<br>phases, implementation</li>
      <li class="topic-highlight">Job bank: bring your CV!</li>
    </ul>
  </section>

  <p class="event-info">Thursday 20th June, <span class="event-time">00:00 h</span> at the Escuela de Sistemas, Instituto Pelayo Norte.</p>
</main>
</body>
</html>
```